Tidal-Cup Coffee Kiosks Webdesign project

Tidal-Cup Coffee Kiosks provides coffee carts, kiosks, and/or drive thrus depending on location. At Tidal-Cup our company focuses on offering healthy snack & drink options for people on the go as well as nutritional coaching with our daily "Cup notes." We will provide some healthy snacks as well.

We offer all organic coffee & espresso drinks,100% real fruit & vegetable smoothies, protein shakes, and healthy breakfast/snack items.

I want "balance" to be a big theme in the website design. True well-being is a balance of body (health), mind (emotional well-being) and spirit (we are a Christian based company who loves and accepts all people, sexual orientation, religions, ect)

My parents are missionaries and founded the Nicaraguan organization "Bright Harvest Outreach Nicaragua" over 11 years ago ( www.brightharvestout.org ). Tidal-Cup plans to be a financial partner to their mission so 10% of profits or 2% of total revenue, whichever is greater will go to Bright Harvest and their church plants & medical/dental clinic. I want this and info about Bright Harvest to have a page on the website.
Updates

Target Market(s)

Ages 18-54 (target coffee customer).

Industry/Entity Type

Financial

Requirements
Must have
• -Home page
-Menu page
-Locations page/contact page
-Kiosk options page (cart, kiosk & drive thru descriptions, pics, traffic & location needs, ect)
-Fundraising/Bright Harvest Outreach Nicaragua page
Nice to have
• I have a logo designed that I attached. I would like the colors to be dark brown, light brown, and a lime green. My business card is also attached.

```html
<!DOCTYPE html>
<html lang="en">
<head>
<meta charset="utf-8">
<title>Tidal-Cup Coffee Kiosks</title>
<link href="https://fonts.googleapis.com/css2?family=Rosarivo&family=Tinos:ital,wght@0,400;0,700;1,700&family=Delius&family=Arimo:wght@700&display=swap" rel="stylesheet">
<style>
:root{
  --burlap:#d8cab6;
  --burlap-dark:#c9b89f;
  --wine:#6a191c;
  --wine-dark:#3a1812;
  --cart-border:#a24a3c;
  --ink:#1a0f0a;
  --brown:#3b2314;
  --cream:#f4ece0;
  --lime:#8dc63f;
  --frame:#8a8580;
  --panel:rgba(255,255,255,.35);
  --button:#7a3d39;
}
*{margin:0;padding:0;box-sizing:border-box}
html,body{width:1200px;height:1032px;overflow:hidden}
body{
  position:relative;
  background:radial-gradient(ellipse at 50% 40%,var(--burlap) 0%,var(--burlap-dark) 100%);
  font-family:"Tinos",serif;color:var(--ink);
}
.abs{position:absolute}
.logo{left:85px;top:30px;display:flex;align-items:center;gap:10px}
.logo-dot{width:40px;height:40px;border-radius:50%;background:var(--brown)}
.logo-name{font-family:"Rosarivo",serif;font-size:38px;color:var(--brown)}
.top-nav{top:22px;left:561px;display:flex;gap:25px;font-size:14.5px}
.top-nav a{color:var(--ink);text-decoration:none}
.partner-badge{left:670px;top:58px;width:122px;height:52px;border-radius:6px;background:rgba(40,40,100,.25)}
.cart{left:817px;top:62px;width:308px;height:42px;background:var(--wine-dark);border:2px solid var(--cart-border);color:var(--cream);font-size:11px;line-height:14px;padding:5px 0 0 58px}
.cart svg{position:absolute;left:14px;top:8px}
.main-band{left:0;top:122px;width:1200px;height:54px;background:var(--wine)}
.main-nav{left:99px;top:134px;display:flex;gap:39px;font-family:"Rosarivo",serif;font-size:19.3px;color:var(--cream)}
.search-box{left:873px;top:138px;width:167px;height:23px;background:#fff;box-shadow:3px 3px 4px rgba(0,0,0,.5)}
.search-label{left:1054px;top:137px;font-family:"Rosarivo",serif;font-size:20px;color:var(--cream)}
.hero{left:95px;top:193px;width:678px;height:232px;background:#040605}
.hero-photo{position:absolute;left:50px;top:20px;width:140px;height:200px;background:radial-gradient(ellipse at center,#7a3a20 0%,#2a120a 55%,#040605 80%)}
.hero-title{position:absolute;left:273px;top:33px;font-family:"Delius",cursive;font-size:13px;color:#eee}
.hero-copy{position:absolute;left:225px;top:65px;width:400px;text-align:center;font-size:12.5px;line-height:16px;color:#eee}
.hero-sign{position:absolute;left:486px;top:196px;font-family:"Delius",cursive;font-size:13px;color:var(--lime)}
.product{position:absolute}
.product-photo{border:2px solid var(--frame);background:#fff;display:block}
.product-caption{text-align:center;font-size:14px;line-height:16px;margin-top:24px}
.newsletter{left:449px;top:701px;width:331px;height:157px;background:var(--panel);border:1px solid rgba(255,255,255,.5);font-family:"Arimo",sans-serif;font-weight:700;padding:14px 0 0 23px}
.newsletter h2{font-size:18px;color:var(--wine);margin-bottom:11px}
.newsletter label{font-size:14px;display:block;margin-bottom:8px}
.newsletter .field{width:284px;height:31px;background:#fff;border:2px solid #999}
.newsletter .subscribe{margin:10px 0 0 61px;width:167px;height:28px;background:linear-gradient(#8e4a45,var(--button));color:#fff;font-size:14px;text-align:center;line-height:28px;box-shadow:3px 3px 4px rgba(0,0,0,.4)}
.side-title{left:813px;top:205px;width:220px;font-style:italic;font-weight:700;font-size:18px;line-height:17px;color:var(--brown);text-align:center}
.side-list{left:808px;top:268px;width:300px;font-size:15.5px;line-height:16px;list-style:none;white-space:nowrap}
.side-list li{position:relative;padding-left:13px}
.side-list li::before{content:"";position:absolute;left:0;top:6px;width:6px;height:6px;border-radius:50%;background:var(--lime)}
.side-photo{left:822px;top:490px;width:256px;height:430px;border-radius:20px 20px 40px 40px;background:linear-gradient(#2a1a12 0%,#2a1a12 35%,#d9782a 36%,#c9641e 100%)}
.footer{left:0;top:967px;width:1200px;height:65px;background:var(--wine);color:var(--cream);font-family:"Rosarivo",serif;font-size:20px;padding:21px 0 0 90px}
</style>
</head>
<body>
<div class="abs logo"><span class="logo-dot"></span><span class="logo-name">Tidal-Cup</span></div>
<nav class="abs top-nav"><a>Our Bean Story</a><a>Locations</a><a>Store</a><a>Menu</a><a>Franchising</a><a>Fundraising</a><a>Contact Us</a></nav>
<div class="abs partner-badge" role="img" aria-label="Bright Harvest Outreach Nicaragua partner badge"></div>
<div class="abs cart">
  <svg width="28" height="26" viewBox="0 0 28 26" fill="none" stroke="#f4ece0" stroke-width="2"><path d="M1 2h5l4 14h13l3-10H8"/><circle cx="11" cy="21" r="2"/><circle cx="21" cy="21" r="2"/></svg>
  Checkout | Login / Register | My Cart<br>(Your Shopping Cart is Empty)
</div>
<div class="abs main-band"></div>
<nav class="abs main-nav"><span>Shop for Coffee</span><span>Shop Coffee Necessities</span><span>Shop for Gifts</span><span>Shop for Tea</span></nav>
<div class="abs search-box"></div>
<div class="abs search-label">Search</div>

<section class="abs hero">
  <div class="hero-photo" role="img" aria-label="Chocolate drink topped with cream beside strawberries"></div>
  <p class="hero-title">Balance for body, mind and spirit daily</p>
  <p class="hero-copy">organic coffee and espresso drinks, real fruit<br>and vegetable smoothies, protein shakes<br>and healthy breakfast and snack items served from<br>carts, kiosks and drive thrus near you. Every visit<br>helps Bright Harvest Outreach Nicaragua<br>fund church plants and a clinic.<br>Read our daily Cup notes.</p>
  <p class="hero-sign">Tidal-Cup.</p>
</section>

<div class="product" style="left:90px;top:441px;width:142px"><div class="product-photo" style="height:156px;background:linear-gradient(#fff,#e8efe6)" role="img" aria-label="Bag of organic coffee beans with a cup"></div><p class="product-caption">Organic Coffee<br>House Roast Bag<br>Rs. $12.90<br>Buy Now</p></div>
<div class="product" style="left:262px;top:441px;width:153px"><div class="product-photo" style="height:156px;background:radial-gradient(circle,#b58a5e 0%,#fff 45%)" role="img" aria-label="Cappuccino in a white cup"></div><p class="product-caption">Cappuccino<br>Organic Espresso<br>Rs. $12.90<br>Buy Now</p></div>
<div class="product" style="left:449px;top:441px;width:149px"><div class="product-photo" style="height:156px;background:linear-gradient(90deg,#fff 5%,#d8463a 35%,#7bb04a 65%,#fff 95%)" role="img" aria-label="Red and green vegetable smoothies"></div><p class="product-caption">Veggie Smoothie<br>Real Fruit &amp; Greens<br>Rs. $12.90<br>Buy Now</p></div>
<div class="product" style="left:625px;top:441px;width:148px"><div class="product-photo" style="height:156px;background:radial-gradient(circle,#e7b04a 0%,#f3d9b0 40%,#fff 75%)" role="img" aria-label="Plates of healthy breakfast snacks"></div><p class="product-caption" style="margin-top:20px">Breakfast Bites<br>Healthy Snack Plate<br>Rs. $12.90<br>Buy Now</p></div>
<div class="product" style="left:94px;top:699px;width:141px"><div class="product-photo" style="height:159px;background:linear-gradient(#f5f1ea 20%,#a57c55 60%,#ddd 90%)" role="img" aria-label="Latte in a glass cup"></div><p class="product-caption">Organic Latte<br>Steamed Milk Latte<br>Rs. $12.90<br>Buy Now</p></div>
<div class="product" style="left:266px;top:699px;width:141px"><div class="product-photo" style="height:159px;background:linear-gradient(90deg,#fff,#e6a0a8 30%,#7a4a34 55%,#eed9a0 80%,#fff)" role="img" aria-label="Three fruit and protein shakes"></div><p class="product-caption">Protein Shakes<br>Fruit &amp; Protein Mix<br>Rs. $12.90<br>Buy Now</p></div>

<form class="abs newsletter">
  <h2>Signup for our Newsletter</h2>
  <label>Email Address:</label>
  <div class="field"></div>
  <div class="subscribe">Subscribe</div>
</form>

<h2 class="abs side-title">Kiosk options for<br>every location</h2>
<ul class="abs side-list">
  <li>Coffee carts: compact units for<br>lobbies, campuses and events with<br>steady daily foot traffic</li>
  <li>Kiosks: a full menu for malls and<br>transit hubs with high visibility</li>
  <li>Drive thrus: quick service on busy<br>commuter roads with easy access</li>
  <li>Ask about traffic needs</li>
  <li style="margin-top:8px">Bright Harvest: 10% of profits or 2%<br>of revenue goes to church plants<br>and the medical and dental clinic</li>
  <li>See our Fundraising page</li>
</ul>
<div class="abs side-photo" role="img" aria-label="Coffee being poured into an orange paper cup"></div>

<footer class="abs footer">Copyright @ Tidal-Cup. All Rights Reserved</footer>
</body>
</html>
```